KEV.PRO- Darren Holcombe Fitness- needs a clever business card using the logo, name, info, contact

I need a business card designed for my Online Personal Training company called KEV.PRO, abbreviation for Darren Holcombe Fitness. My company focuses on coaching in personal health and personal growth to unleash your greatest potential. I would like to see designs that use my color scheme of a redish-orange (C:0,M:84,Y:100,K:0), grey, white, black, and my company font is OSWALD. The final design should communicate some aspects of design, health, motivation, growth, in some way. The logo is very important to the company and can be displayed in any of the colors previously mentioned. Must include the company name, my website: www.kev-pro.example , my email: dan@kev-pro.example

Target Market(s)

Personal health, fitness, general public, those who lack knowledge, awareness, and confidence in personal health

Industry/Entity Type

Personal Trainer

Font styles to use
Other font styles liked:
• OSWALD. (Bold, Regular, Light)

Colors
f37122
ffffff
9d9d9d
000000

Requirements
Must have
• Must include the logo, company name, my website: www.kev-pro.example , my email: dan@kev-pro.example
Nice to have
• Variations of the colors scheme of a redish-orange (C:0,M:84,Y:100,K:0), grey, white, black. Logo, card, or text can be in any of these colors.
• Possible quote like "Take control of your personal health to unleash your greatest potential" or "Unleashing your greatness first begins with fitness of the body and mind"

```html
<!DOCTYPE html>
<html lang="en">
<head>
<meta charset="utf-8">
<title>KEV.PRO Business Card</title>
<link rel="stylesheet" href="https://fonts.googleapis.com/css2?family=Oswald:wght@400&family=Open+Sans:wght@400;600&display=swap">
<style>
  :root {
    --orange: #f0521f;
    --white: #ffffff;
    --grey: #9d9d9d;
    --card: #050505;
    --stage: #2e2925;
  }
  * { margin: 0; padding: 0; box-sizing: border-box; }
  html, body { width: 1200px; height: 844px; overflow: hidden; }
  body {
    background: var(--stage);
    position: relative;
    font-family: "Open Sans", Arial, sans-serif;
    color: var(--white);
  }
  .card {
    position: absolute;
    top: 272px;
    width: 520px;
    height: 300px;
    background: radial-gradient(ellipse at 50% 30%, #1a1a1a 0%, var(--card) 70%);
    overflow: hidden;
    box-shadow: 0 10px 30px rgba(0,0,0,.45);
  }
  .card--contact { left: 50px; }
  .card--brand { left: 630px; }

  /* contact side */
  .band {
    position: absolute;
    left: 0; right: 0;
    height: 11px;
    background: var(--orange);
  }
  .band--top { top: 16px; }
  .band--bottom { bottom: 16px; }
  .contact-block {
    position: absolute;
    left: 0; right: 0;
    top: 78px;
    text-align: center;
  }
  .person-name {
    display: inline-block;
    font-family: "Oswald", Arial, sans-serif;
    font-weight: 400;
    font-size: 19px;
    letter-spacing: .5px;
    color: var(--orange);
    padding: 0 4px 1px;
    border-bottom: 1px solid var(--orange);
  }
  .person-role { font-size: 13px; margin-top: 2px; }
  .contact-lines { margin-top: 30px; font-size: 13px; line-height: 18px; }
  .address { margin-top: 34px; font-size: 13px; }

  /* brand side */
  .tab {
    position: absolute;
    width: 30px;
    height: 34px;
    background: var(--orange);
  }
  .tab::after {
    content: "";
    position: absolute;
    top: 0; bottom: 0;
    left: -6px;
    width: 4px;
    background: linear-gradient(90deg, var(--white), var(--grey));
  }
  .tab--right { right: 12px; top: 22px; }
  .tab--left { left: 12px; top: 150px; }
  .brand-name {
    position: absolute;
    left: 0; right: 0;
    top: 96px;
    text-align: center;
    font-family: "Open Sans", Arial, sans-serif;
    font-weight: 600;
    font-size: 22px;
    letter-spacing: 2px;
    color: var(--white);
  }
  .tagline {
    position: absolute;
    left: 0; right: 0;
    top: 196px;
    text-align: center;
    font-weight: 600;
    font-size: 14px;
    line-height: 18px;
    text-transform: uppercase;
    color: var(--white);
  }
</style>
</head>
<body>
  <section class="card card--contact">
    <div class="band band--top"></div>
    <div class="contact-block">
      <div class="person-name">MARCUS BELL</div>
      <div class="person-role">Managing Director</div>
      <div class="contact-lines">
        <div>055-321-9087</div>
        <div>dan@kev-pro.example</div>
        <div>www.kev-pro.example</div>
      </div>
      <div class="address">88 Harbor Lane | Westfield, AB | 654321</div>
    </div>
    <div class="band band--bottom"></div>
  </section>

  <section class="card card--brand">
    <div class="tab tab--right"></div>
    <div class="tab tab--left"></div>
    <div class="brand-name">KEV.PRO</div>
    <p class="tagline">Take control of your personal health to unleash<br>your greatest potential</p>
  </section>
</body>
</html>
```